Ferncrest Dental, LLC business card project

Business card to be designed with current logo.
Dental office- please keep design of card that looks clean and professional.
Please include the following info:
Ferncrest Dental, LLC
Dr. Lorna Pettigrew
2871 Marlowe Street
Marrowdale, OR 97093
541-555-0193
ferncrestdental.office@examplemail.test
Hello everyone-
Reason: Just got back from overseas- will look at all designs and provide feedback. Thank you!
Reason: Polling my friends for the final selection-
thank you to all those that participated- so many talented designers!

```html
<!DOCTYPE html>
<html lang="en">
<head>
<meta charset="utf-8">
<title>Ferncrest Dental, LLC — Business Card</title>
<link rel="stylesheet" href="https://fonts.googleapis.com/css2?family=Arimo:wght@400;700&display=swap">
<style>
  :root {
    --card-dark: #2a2a28;
    --card-mid: #5b5b57;
    --band-dark: #232323;
    --accent-orange: #f57c0a;
    --brand-green: #8cc63e;
    --text-light: #f4f4f4;
    --text-shadow: rgba(0, 0, 0, 0.85);
  }
  * { margin: 0; padding: 0; box-sizing: border-box; }
  html, body { width: 1200px; height: 639px; overflow: hidden; background: #1a1a1a; }
  body { font-family: "Arimo", Arial, sans-serif; }

  .card {
    position: relative;
    width: 1200px;
    height: 639px;
    overflow: hidden;
    background:
      radial-gradient(ellipse 620px 220px at 560px 470px, var(--card-mid), transparent 75%),
      linear-gradient(180deg, #333331 0%, var(--card-dark) 45%, #3c3c39 100%);
  }

  .brand-name {
    position: absolute;
    display: flex;
    align-items: center;
    color: var(--brand-green);
    font-weight: 400;
    white-space: nowrap;
  }
  .brand-name .brand-dot {
    display: inline-block;
    border-radius: 50%;
    background: var(--brand-green);
  }
  .brand-main { left: 42px; top: 70px; font-size: 54px; gap: 18px; }
  .brand-main .brand-dot { width: 26px; height: 26px; }
  .brand-corner { right: 20px; top: 30px; font-size: 25px; gap: 9px; }
  .brand-corner .brand-dot { width: 13px; height: 13px; }

  .arrow-art {
    position: absolute;
    right: 0;
    top: 280px;
    width: 360px;
    height: 216px;
    background: radial-gradient(ellipse 200px 150px at 65% 75%, rgba(245, 124, 10, 0.45), rgba(245, 124, 10, 0) 80%);
  }

  .contact-list {
    position: absolute;
    left: 42px;
    top: 282px;
    list-style: none;
    color: var(--text-light);
    font-size: 27px;
    text-shadow: 1px 2px 2px var(--text-shadow);
  }
  .contact-list li {
    display: flex;
    align-items: center;
    height: 45px;
  }
  .contact-list svg { width: 14px; height: 14px; margin-right: 8px; flex: none; }

  .accent-band {
    position: absolute;
    left: 0; top: 496px;
    width: 1200px; height: 53px;
    background: var(--accent-orange);
    box-shadow: 0 -10px 18px rgba(0, 0, 0, 0.35);
  }

  .footer-band {
    position: absolute;
    left: 0; top: 549px;
    width: 1200px; height: 90px;
    background: var(--band-dark);
    display: flex;
    align-items: center;
    justify-content: space-between;
    padding: 0 52px 0 54px;
  }
  .footer-phone {
    font-size: 36px;
    font-weight: 700;
    color: #e6e6e6;
    background: linear-gradient(180deg, #ffffff 0%, #d0d0d0 55%, #9a9a9a 100%);
    -webkit-background-clip: text;
    background-clip: text;
    -webkit-text-fill-color: transparent;
    filter: drop-shadow(1px 2px 1px rgba(0, 0, 0, 0.9));
  }
  .footer-email {
    font-size: 29px;
    color: var(--text-light);
    white-space: nowrap;
  }
</style>
</head>
<body>
  <div class="card">
    <div class="brand-name brand-main"><span class="brand-dot"></span>Ferncrest Dental, LLC</div>
    <div class="brand-name brand-corner"><span class="brand-dot"></span>Ferncrest Dental, LLC</div>

    <div class="arrow-art" role="img" aria-label="Rising orange arrows decoration"></div>

    <ul class="contact-list">
      <li><svg viewBox="0 0 14 14"><path d="M1 5.5h6V2l6 5-6 5V8.5H1z" fill="#f57c0a"/></svg>Dr. Lorna Pettigrew</li>
      <li><svg viewBox="0 0 14 14"><path d="M1 5.5h6V2l6 5-6 5V8.5H1z" fill="#f57c0a"/></svg>2871 Marlowe Street</li>
      <li><svg viewBox="0 0 14 14"><path d="M1 5.5h6V2l6 5-6 5V8.5H1z" fill="#f57c0a"/></svg>Marrowdale, OR 97093</li>
      <li><svg viewBox="0 0 14 14"><path d="M1 5.5h6V2l6 5-6 5V8.5H1z" fill="#f57c0a"/></svg>Ferncrest Dental, LLC</li>
    </ul>

    <div class="accent-band"></div>

    <div class="footer-band">
      <span class="footer-phone">Tel:541-555-0193</span>
      <span class="footer-email">E.mail:ferncrestdental.office@examplemail.test</span>
    </div>
  </div>
</body>
</html>
```